Chartered Professional Accounting Firm Needs a Business Card Design

We need a card design for an accounting firm based in Toronto, Ontario. The firm name is Lorne Patek Professional Corporation. The owner of the firm is a chartered professional accountant and a certified general accountant. Services of the firm include 60% tax preparation and consulting and 40% financial statements for corporation year-end. We would like a modern design. The color could be black, white, gray, blue or other color to bring more confidence to clients. The logo of the firm should be included in the design. Thanks
Updates

Name: Lorne Patek, CPA, CGA Address: 47 Marrow Creek Rd. Richmond Hill, ON K7T 5P3 Telephone: (416) 555-0142 Fax:(416) 555-0187 Email: lorne@lornepatek.example

Industry/Entity Type

Accounting

```html
<!DOCTYPE html>
<html lang="en">
<head>
<meta charset="utf-8">
<title>Lorne Patek Professional Corporation – Business Card</title>
<link rel="stylesheet" href="https://fonts.googleapis.com/css2?family=Montserrat:wght@700&family=Questrial&display=swap">
<style>
  :root {
    --card-bg: #ffffff;
    --brand-blue: #0714e8;
    --text-gray: #7b8787;
  }
  html, body {
    margin: 0;
    padding: 0;
    width: 1200px;
    height: 777px;
    overflow: hidden;
    background: var(--card-bg);
  }
  .card {
    position: relative;
    width: 1200px;
    height: 777px;
    background: var(--card-bg);
    font-family: "Questrial", "Century Gothic", sans-serif;
    color: var(--text-gray);
  }
  .card p, .card h1 {
    position: absolute;
    left: 68px;
    margin: 0;
    line-height: 1;
    white-space: nowrap;
  }
  .owner-name {
    top: 34px;
    font-family: "Montserrat", "Century Gothic", sans-serif;
    font-weight: 700;
    font-size: 108px;
    letter-spacing: 1px;
    color: var(--brand-blue);
  }
  .owner-title {
    top: 150px;
    font-size: 42px;
  }
  .firm-name {
    top: 212px;
    font-size: 38px;
    color: var(--brand-blue);
    display: flex;
    align-items: center;
    gap: 14px;
  }
  .firm-mark {
    display: inline-block;
    width: 26px;
    height: 26px;
    background: var(--brand-blue);
  }
  .address-line,
  .contact-line {
    font-size: 56px;
  }
  .address-street { top: 292px; }
  .address-city   { top: 356px; }
  .address-postal { top: 420px; }
  .contact-phone  { top: 516px; }
  .contact-fax    { top: 580px; }
  .contact-email  { top: 656px; }
</style>
</head>
<body>
  <main class="card">
    <h1 class="owner-name">Lorne Patek</h1>
    <p class="owner-title">Chartered Professional Accountant, CPA, CGA</p>
    <p class="firm-name"><span class="firm-mark"></span>Lorne Patek Professional Corporation</p>
    <p class="address-line address-street">47 Marrow Creek Rd.</p>
    <p class="address-line address-city">Richmond Hill, Ontario</p>
    <p class="address-line address-postal">K7T 5P3</p>
    <p class="contact-line contact-phone">(416) 555-0142 (tel)</p>
    <p class="contact-line contact-fax">(416) 555-0187 (fax)</p>
    <p class="contact-line contact-email">lorne@lornepatek.example</p>
  </main>
</body>
</html>
```